Business Consulting Business Card

professional business card with basic information (1) First and Last name (2) email address, (3) phone number, (4) website.

```html
<!DOCTYPE html>
<html lang="en">
<head>
<meta charset="utf-8">
<title>Tidemark Business Card</title>
<link href="https://fonts.googleapis.com/css2?family=Figtree:wght@400;500;700&display=swap" rel="stylesheet">
<style>
  :root {
    --navy: #062a3d;
    --ink: #0b2d42;
    --teal: #3aaabf;
    --paper: #ffffff;
    --stage: #ffffff;
    --muted: #5b6670;
  }
  * { box-sizing: border-box; margin: 0; padding: 0; }
  html, body {
    width: 1200px; height: 1134px; overflow: hidden;
    background: var(--stage);
    font-family: "Figtree", sans-serif;
  }
  .sheet {
    position: relative; width: 1200px; height: 1134px;
  }
  .card {
    position: absolute; left: 142px; width: 915px; height: 523px;
    border-radius: 22px; overflow: hidden;
    box-shadow: 0 2px 8px rgba(0,0,0,0.25);
  }
  .card--front { top: 20px; background: var(--paper); }
  .card--back { top: 591px; background: var(--navy); }

  .brand { position: absolute; display: flex; align-items: center; }
  .brand__dot { border-radius: 50%; background: var(--teal); flex: none; }
  .brand__name { font-weight: 500; text-transform: uppercase; }

  .card--front .brand { left: 42px; top: 40px; }
  .card--front .brand__dot { width: 56px; height: 56px; margin-right: 18px; }
  .card--front .brand__name { font-size: 32px; letter-spacing: 0.28em; color: var(--ink); }

  .band {
    position: absolute; left: 0; right: 0; top: 300px; bottom: 0;
    background: var(--navy);
  }
  .portrait {
    position: absolute; left: 37px; top: 178px;
    width: 234px; height: 234px; border-radius: 50%;
    border: 4px solid var(--paper);
    background: radial-gradient(circle at 50% 35%, #c99a82 0 22%, #3b3a40 23% 30%, #f2f2f2 31% 44%, #1f2f52 45%);
  }
  .identity { position: absolute; left: 306px; top: 186px; }
  .identity__name { font-size: 41px; font-weight: 700; color: var(--ink); letter-spacing: -0.01em; }
  .identity__role { font-size: 26px; color: var(--muted); margin-top: 2px; }

  .contacts { position: absolute; left: 306px; top: 326px; list-style: none; }
  .contacts__item { display: flex; align-items: center; height: 35.5px; color: var(--paper); font-size: 27px; }
  .contacts__icon { width: 32px; height: 28px; margin-right: 12px; flex: none; }

  .card--back .brand { left: 132px; top: 0; bottom: 0; }
  .card--back .brand__dot { width: 118px; height: 118px; margin-right: 36px; background: var(--paper); }
  .card--back .brand__name { font-size: 64px; letter-spacing: 0.3em; color: var(--paper); }
</style>
</head>
<body>
<main class="sheet">
  <section class="card card--front">
    <div class="brand">
      <span class="brand__dot"></span>
      <span class="brand__name">Tidemark</span>
    </div>
    <div class="band"></div>
    <div class="portrait" role="img" aria-label="Portrait photo of Marcus Ellery"></div>
    <div class="identity">
      <h1 class="identity__name">Marcus Ellery</h1>
      <p class="identity__role">Managing Broker</p>
    </div>
    <ul class="contacts">
      <li class="contacts__item">
        <svg class="contacts__icon" viewBox="0 0 32 28" fill="none" stroke="var(--teal)" stroke-width="1.6" stroke-linejoin="round">
          <path d="M9 4h20v12H19l-4 4v-4H9z"/><path d="M9 10H3v11h3v4l4-4h9v-5"/>
        </svg>
        (305) 555-0142
      </li>
      <li class="contacts__item">
        <svg class="contacts__icon" viewBox="0 0 32 28" fill="none" stroke="var(--teal)" stroke-width="1.6" stroke-linejoin="round">
          <rect x="2" y="5" width="28" height="19"/><path d="M2 5l14 11L30 5"/>
        </svg>
        mellery@tidemark.com
      </li>
      <li class="contacts__item">
        <svg class="contacts__icon" viewBox="0 0 32 28" fill="none" stroke="var(--teal)" stroke-width="1.6">
          <circle cx="16" cy="14" r="12"/><ellipse cx="16" cy="14" rx="5" ry="12"/><path d="M4 14h24M6 8h20M6 20h20"/>
        </svg>
        www.tidemark.com
      </li>
    </ul>
  </section>

  <section class="card card--back">
    <div class="brand">
      <span class="brand__dot"></span>
      <span class="brand__name">Tidemark</span>
    </div>
  </section>
</main>
</body>
</html>
```